Design revision of an existing Executive Summary

Our company velmora is specialized in the field of performance engineering (load and performance testing as well as application performance monitoring). We are looking for a designer who could graphically "spice up" our current executive summary about our company velmora (www.velmora-it.example). Maybe it would be possible to incorporate a pic of our website (e.g. https://www.velmora-it.example/en/services/performance/) into this newly designed executive summary.

Attached you will find the current executive summary which should not change textually. It should just look fresher and more modern. Ideally, a visually appealing first / title page would precede the text.

```html
<!DOCTYPE html>
<html lang="en">
<head>
<meta charset="utf-8">
<title>velmora – Executive Summary</title>
<link rel="stylesheet" href="https://fonts.googleapis.com/css2?family=Barlow+Semi+Condensed:wght@600&family=Montserrat:wght@300;400&family=Roboto:wght@400;500;700&display=swap">
<style>
  :root {
    --backdrop: #d6d8d8;
    --paper: #ffffff;
    --ink-black: #05060a;
    --navy: #1a3e73;
    --sky: #5bb8dc;
    --photo-top: #24385c;
    --photo-bottom: #0a1120;
    --text-light: #ffffff;
  }
  * { box-sizing: border-box; margin: 0; padding: 0; }
  html, body { width: 1200px; height: 840px; overflow: hidden; background: var(--backdrop); }
  body { position: relative; font-family: "Roboto", Arial, sans-serif; }

  .page { position: absolute; top: 33px; width: 541px; height: 773px; overflow: hidden; }
  .page--cover { left: 43px; background: var(--paper); }
  .page--summary { left: 616px; background: var(--ink-black); }
  .page-shapes { position: absolute; inset: 0; width: 100%; height: 100%; }

  .cover-brand {
    position: absolute; left: 0; right: 0; top: 388px; text-align: center;
    font-family: "Montserrat", sans-serif; font-weight: 300; font-size: 60px;
    color: var(--text-light); letter-spacing: 1px;
  }
  .tagline {
    position: absolute; left: 0; right: 0; text-align: center;
    font-family: "Montserrat", sans-serif; font-weight: 400; color: var(--navy);
  }
  .page--cover .tagline { top: 678px; font-size: 15px; }
  .cover-rule { position: absolute; left: 40px; width: 465px; top: 724px; height: 2px; background: var(--sky); }

  .contact-line {
    position: absolute; left: 0; right: 0; display: flex; justify-content: center; gap: 9px;
    font-size: 8.6px; white-space: nowrap;
  }
  .contact-line span { display: inline-flex; align-items: center; gap: 3px; }
  .contact-line svg { width: 7px; height: 7px; }
  .page--cover .contact-line { top: 738px; color: var(--navy); }
  .page--summary .contact-line { top: 740px; color: var(--text-light); }

  .summary-brand {
    position: absolute; left: 0; right: 0; top: 40px; text-align: center;
    font-family: "Montserrat", sans-serif; font-weight: 400; font-size: 34px; color: var(--navy);
  }
  .page--summary .tagline { top: 88px; font-size: 13px; }

  .section { position: absolute; color: var(--text-light); }
  .section h2 {
    font-family: "Barlow Semi Condensed", sans-serif; font-weight: 600; font-size: 17px;
    letter-spacing: .4px; line-height: 1;
  }
  .section h2::after { content: ""; display: block; width: 64px; height: 2px; background: var(--sky); margin-top: 12px; }
  .section p { font-size: 8.9px; line-height: 12.7px; margin-top: 12px; }
  .section p + p { margin-top: 12.5px; }
  .col-left { left: 33px; width: 218px; }
  .col-right { left: 297px; width: 212px; }
  .who { top: 183px; }
  .team { top: 434px; }
  .services { top: 183px; }

  .service { position: absolute; left: 297px; width: 212px; color: var(--text-light); }
  .service h3 {
    display: flex; align-items: center; gap: 8px;
    font-size: 11.6px; font-weight: 500; color: var(--sky);
  }
  .service h3 svg { flex: none; }
  .service p { font-size: 8.9px; line-height: 12.7px; margin-top: 14px; }
  .service--load { top: 213px; }
  .service--apm { top: 364px; }
  .service--training { top: 504px; }

  .customers-title {
    position: absolute; left: 0; right: 0; top: 653px; text-align: center;
    font-family: "Barlow Semi Condensed", sans-serif; font-weight: 600; font-size: 15px;
    color: var(--text-light); letter-spacing: .4px;
  }
  .customers {
    position: absolute; left: 0; right: 0; top: 667px; height: 54px; background: var(--paper);
    display: flex; align-items: center; justify-content: space-between; padding: 0 30px 0 32px;
  }
  .customer { display: inline-flex; align-items: center; gap: 4px; font-weight: 700; font-size: 11px; color: var(--navy); }
  .customer i { display: inline-block; width: 7px; height: 7px; background: var(--navy); }
</style>
</head>
<body>

<!-- Title page -->
<section class="page page--cover">
  <svg class="page-shapes" viewBox="0 0 1035 1477" preserveAspectRatio="none">
    <defs>
      <linearGradient id="cityTone" x1="0" y1="0" x2="0" y2="1">
        <stop offset="0" stop-color="var(--photo-top)"/>
        <stop offset="1" stop-color="var(--photo-bottom)"/>
      </linearGradient>
    </defs>
    <rect x="0" y="0" width="1035" height="1320" fill="url(#cityTone)" role="img" aria-label="Night city skyline with light trails on a highway, tinted dark blue"/>
    <polygon points="0,1254 418,1206 1035,1306 1035,1477 0,1477" fill="var(--paper)"/>
    <polygon points="0,1136 418,1206 0,1254" fill="var(--navy)"/>
    <polygon points="418,1206 1035,1130 1035,1306" fill="var(--sky)"/>
  </svg>
  <div class="cover-brand">velmora</div>
  <p class="tagline">Performance matters.</p>
  <div class="cover-rule"></div>
  <div class="contact-line">
    <span><svg viewBox="0 0 10 10"><path d="M2 1l2 2-1 1.5c.6 1.2 1.4 2 2.5 2.5L7 6l2 2-1.5 1.5C5 9 1 5 .5 2z" fill="var(--sky)"/></svg>+43 - 1 - 55 01 23 0000</span>
    <span><svg viewBox="0 0 10 10"><rect x=".5" y="2" width="9" height="6" fill="none" stroke="var(--sky)"/><path d="M.5 2l4.5 3.5L9.5 2" fill="none" stroke="var(--sky)"/></svg>office@velmora-it.example</span>
    <span><svg viewBox="0 0 10 10"><circle cx="5" cy="5" r="4.3" fill="none" stroke="var(--sky)"/><path d="M.7 5h8.6M5 .7c-2.4 2.6-2.4 6 0 8.6M5 .7c2.4 2.6 2.4 6 0 8.6" fill="none" stroke="var(--sky)" stroke-width=".8"/></svg>www.velmora-it.example</span>
    <span><svg viewBox="0 0 10 10"><rect x="1" y="1" width="8" height="8" fill="var(--sky)"/></svg>www.proflink.example/company/velmora</span>
  </div>
</section>

<!-- Summary page -->
<section class="page page--summary">
  <svg class="page-shapes" viewBox="0 0 1035 1477" preserveAspectRatio="none">
    <polygon points="0,0 1035,0 1035,168 430,270 0,212" fill="var(--paper)"/>
    <polygon points="0,212 430,270 0,340" fill="var(--navy)"/>
    <polygon points="430,270 1035,168 1035,346" fill="var(--sky)"/>
  </svg>
  <div class="summary-brand">velmora</div>
  <p class="tagline">Performance matters.</p>

  <article class="section col-left who">
    <h2>WHO WE ARE?</h2>
    <p>Velmora is the go-to-company in the very specialized area of performance engineering. Whether microservices in the cloud or legacy on-premise: We will show you the added value of load &amp; performance tests, performance tuning or monitoring solutions.</p>
    <p>In the area of application performance monitoring, we like to work with the enterprise solution from industry leader Tracewell. velmora is Tracewell Premier Partner and therefore amongst an exclusive group of companies in the EMEA region specialized in Tracewell.</p>
  </article>

  <article class="section col-left team">
    <h2>ABOUT OUR TEAM</h2>
    <p>Our performance engineers guide our customers through the whole process of performance testing by providing best practices for test design and test strategies, setting up infrastructure, carrying out performance tests as well as preparing the reporting. If required, our performance engineers go beyond reporting by identifying the actual bottlenecks and even performing code reviews. As we offer to play such an active role in fixing performance defects, all our consultants are well-skilled software engineers.</p>
  </article>

  <article class="section col-right services">
    <h2>OUR SERVICES</h2>
  </article>

  <div class="service service--load">
    <h3>Load &amp; Performance Testing
      <svg width="38" height="38" viewBox="0 0 38 38" fill="none" stroke="var(--sky)" stroke-width="1.4"><path d="M10 14a7 7 0 0 1 13-4 6 6 0 0 1 9 6 4 4 0 0 1-2 8h-4"/><circle cx="17" cy="21" r="6"/><path d="M12.5 25.5L5 33"/></svg>
    </h3>
    <p>An often-neglected necessity to ensure the speed, stability and reliability of your IT applications and digital services. If you expect many users rushing in on your digital roads, performance tests are required to provide the best experience for your customers.</p>
  </div>

  <div class="service service--apm">
    <h3>APM &amp; Observability
      <svg width="46" height="40" viewBox="0 0 46 40" fill="none" stroke="var(--sky)" stroke-width="1.4"><circle cx="24" cy="17" r="11"/><path d="M16 25L5 36"/><path d="M19 22v-4M23 22v-7M27 22v-9M31 22V6"/></svg>
    </h3>
    <p>Follow the experience of users and pinpoint the root-cause of problems as fast as possible in case of an undesired event and get business insights like usage statistics and conversion rates just along the way.</p>
  </div>

  <div class="service service--training">
    <h3>Trainings &amp; Workshops
      <svg width="42" height="42" viewBox="0 0 42 42" fill="none" stroke="var(--sky)" stroke-width="1.4"><rect x="18" y="3" width="20" height="30"/><path d="M22 10h12M22 15h12M22 20h12M22 25h12"/><path d="M6 16l4 22 4-22z"/><circle cx="10" cy="11" r="4"/></svg>
    </h3>
    <p>Enable your own performance testing team by learning innovative approaches such as the automation of quality gates and automate performance feedback or get started with the basic methodology training.</p>
  </div>

  <h2 class="customers-title">VALUED CUSTOMERS</h2>
  <div class="customers">
    <span class="customer">NORDSURE</span>
    <span class="customer">BAUKRAFT</span>
    <span class="customer"><i></i>CITY IT</span>
    <span class="customer">ALVENTA</span>
    <span class="customer">CHAMBERO</span>
    <span class="customer"><i></i>Gemeindenet</span>
  </div>

  <div class="contact-line">
    <span><svg viewBox="0 0 10 10"><path d="M2 1l2 2-1 1.5c.6 1.2 1.4 2 2.5 2.5L7 6l2 2-1.5 1.5C5 9 1 5 .5 2z" fill="var(--sky)"/></svg>+43 - 1 - 55 01 23 0000</span>
    <span><svg viewBox="0 0 10 10"><rect x=".5" y="2" width="9" height="6" fill="none" stroke="var(--sky)"/><path d="M.5 2l4.5 3.5L9.5 2" fill="none" stroke="var(--sky)"/></svg>office@velmora-it.example</span>
    <span><svg viewBox="0 0 10 10"><circle cx="5" cy="5" r="4.3" fill="none" stroke="var(--sky)"/><path d="M.7 5h8.6M5 .7c-2.4 2.6-2.4 6 0 8.6M5 .7c2.4 2.6 2.4 6 0 8.6" fill="none" stroke="var(--sky)" stroke-width=".8"/></svg>www.velmora-it.example</span>
    <span><svg viewBox="0 0 10 10"><rect x="1" y="1" width="8" height="8" fill="var(--sky)"/></svg>www.proflink.example/company/velmora</span>
  </div>
</section>

</body>
</html>
```